Stationery Design needed for logo design project

This project is linked to Logo: brand identity for modern furniture design studio..

Our company needs a Stationery Design. Please refer to our original project in the link above.

```html
<!DOCTYPE html>
<html lang="en">
<head>
<meta charset="utf-8">
<title>Lumora Stationery</title>
<link href="https://fonts.googleapis.com/css2?family=Questrial&family=Arimo:wght@400;700&display=swap" rel="stylesheet">
<style>
  :root {
    --backdrop: #e7e5e1;
    --paper: #ffffff;
    --paper-edge: #d9dcdd;
    --slate: #5d686c;
    --slate-light: #8d9699;
    --ink: #2b2f31;
    --body-ink: #6b7376;
    --rule: #9aa2a5;
  }
  * { margin: 0; padding: 0; box-sizing: border-box; }
  html, body { width: 1200px; height: 1000px; overflow: hidden; }
  body {
    background: var(--backdrop);
    position: relative;
    font-family: "Arimo", Arial, sans-serif;
  }
  .wordmark {
    font-family: "Questrial", "Century Gothic", sans-serif;
    color: var(--slate);
    font-weight: 400;
    letter-spacing: 0.02em;
    line-height: 1;
  }
  .sheet { position: absolute; background: var(--paper); box-shadow: 0 2px 8px rgba(0,0,0,0.12); }

  /* Letterhead */
  .letterhead { left: 50px; top: 50px; width: 460px; height: 650px; padding: 70px 60px; }
  .letterhead .wordmark { font-size: 44px; margin-bottom: 50px; }
  .letterhead p {
    font-size: 12px; line-height: 1.75; color: var(--body-ink); margin-bottom: 16px;
  }

  /* Note block */
  .note-block { left: 570px; top: 50px; width: 260px; height: 260px;
    display: flex; align-items: center; justify-content: center;
    box-shadow: 0 2px 0 #ececec, 0 4px 0 #e2e2e2, 0 6px 0 #dcdcdc, 0 8px 10px rgba(0,0,0,0.15); }
  .note-block .wordmark { font-size: 46px; color: var(--slate-light); }

  /* Business card */
  .business-card { left: 870px; top: 80px; width: 290px; height: 170px; display: flex; overflow: hidden; }
  .business-card .card-band {
    width: 70px; background: var(--slate); position: relative;
  }
  .business-card .card-band .wordmark {
    position: absolute; left: 50%; top: 50%;
    transform: translate(-50%, -50%) rotate(-90deg);
    font-size: 32px; color: var(--slate-light);
  }
  .business-card .card-info { flex: 1; padding: 16px 16px; color: var(--ink); }
  .card-name { font-weight: 700; font-size: 16px; letter-spacing: 0.05em; }
  .card-tagline { font-size: 8px; color: var(--body-ink); margin: 2px 0 12px; }
  .card-contact { list-style: none; font-size: 10px; font-weight: 700; line-height: 1.5; }
  .card-contact span { display: inline-block; width: 16px; font-weight: 400; color: var(--body-ink); }
  .card-social { list-style: none; font-size: 10px; font-weight: 700; line-height: 1.5; margin-top: 6px; }

  /* Envelope */
  .envelope { left: 570px; top: 360px; width: 590px; height: 290px;
    border: 3px solid var(--paper-edge); padding: 40px 44px; }
  .envelope .wordmark { font-size: 48px; }
  .address-lines { position: absolute; right: 60px; bottom: 50px; width: 220px; }
  .address-lines span { display: block; height: 1px; background: var(--rule); margin-top: 26px; }
</style>
</head>
<body>
  <section class="sheet letterhead">
    <div class="wordmark">lumora</div>
    <p>Lorem ipsum dolor sit amet, consectetur adipiscing elit. Donec orci purus, luctus vitae faucibus, ipsum nec dolor aliquet viverra, leo diam ligula quis arcu. Nunc egestas tortor in suscipit a, lacus eros mauris, et scelerisque nisl id massa.</p>
    <p>Duis consequat, magna eget ultrices varius, Vestibulum nunc vel fringilla nisi eros. Aliquam erat volutpat, sed vitae risus inter dum. Pellentesque quam, a id vehicula sem, rhoncus nec ac eros mauris.</p>
    <p>Integer facilisis, nulla vel tempor blandit, turpis purus dictum lectus, sed porta quam felis at lorem. Curabitur sit amet.</p>
  </section>

  <section class="sheet note-block">
    <div class="wordmark">lumora</div>
  </section>

  <section class="sheet business-card">
    <div class="card-band"><div class="wordmark">lumora</div></div>
    <div class="card-info">
      <div class="card-name">LUMORA</div>
      <div class="card-tagline">furniture design studio</div>
      <ul class="card-contact">
        <li><span>T:</span>(720) 555-0187</li>
        <li><span>E:</span>hello@lumora.co.uk</li>
        <li><span>W:</span>www.lumora.co.uk</li>
      </ul>
      <ul class="card-social">
        <li>facebook.com/lumorastudio</li>
        <li>twitter.com/lumorastudio</li>
      </ul>
    </div>
  </section>

  <section class="sheet envelope">
    <div class="wordmark">lumora</div>
    <div class="address-lines"><span></span><span></span><span></span></div>
  </section>
</body>
</html>
```